Makeup Artist Requires Business Card design

Hi

I am looking for a business card design to market my makeup artist business. I operate under my own name Mara Veldt and I would like to keep the design of the card very simplistic and chic - something that keeps both my name and profession (makeup artist) the focus of the card. I would like it to be a style that is eyecatching to the reader (i am open to anything unusual) but upmarket.

Target Market(s)

women, magazine/beauty/fashion editors, photographers.

Industry/Entity Type

Business

Requirements
Must have
• Must contain:

Phone number: 0418 372 915
Website: www.maraveldt.com.au
email: contact@maraveldt.com.au

(although you don't need to have prefaced these with the words phone number, website etc :))
Should not have
• I am not looking for anything overly colorful - my preference is to keep the card dark if possible.

```html
<!DOCTYPE html>
<html lang="en">
<head>
<meta charset="utf-8">
<title>Mara Veldt – Makeup Artist Business Card</title>
<link rel="stylesheet" href="https://fonts.googleapis.com/css2?family=Pinyon+Script&family=Didact+Gothic&display=swap">
<style>
  :root {
    --page-bg: #2a2a2a;
    --card-bg: #1c1c1c;
    --card-edge: #262626;
    --text-soft: #8c8c8c;
    --text-muted: #767676;
    --frame-outer: #6b6b6b;
    --frame-inner: #2b2b2b;
  }
  * { margin: 0; padding: 0; box-sizing: border-box; }
  html, body {
    width: 1200px;
    height: 900px;
    overflow: hidden;
    background: var(--page-bg);
  }
  .canvas {
    position: relative;
    width: 1200px;
    height: 900px;
  }
  .card {
    position: absolute;
    left: 250px;
    width: 700px;
    height: 400px;
    background: linear-gradient(160deg, #222 0%, var(--card-bg) 60%, #191919 100%);
    border: 1px solid var(--card-edge);
    box-shadow: 0 10px 30px rgba(0,0,0,0.55);
  }
  .card--front { top: 35px; }
  .card--back { top: 465px; }

  .brand-name {
    position: absolute;
    left: 60px;
    top: 70px;
    font-family: "Pinyon Script", cursive;
    font-size: 78px;
    color: var(--text-soft);
    font-weight: 400;
    line-height: 1;
  }
  .brand-role {
    position: absolute;
    left: 400px;
    top: 150px;
    font-family: "Didact Gothic", sans-serif;
    font-size: 24px;
    letter-spacing: 1px;
    color: var(--text-muted);
  }

  .portfolio-strip {
    position: absolute;
    display: flex;
    gap: 14px;
  }
  .card--front .portfolio-strip { left: 40px; bottom: 40px; }
  .card--back .portfolio-strip { left: 40px; top: 30px; }

  .portfolio-frame {
    width: 120px;
    height: 104px;
    padding: 5px;
    background: var(--frame-outer);
    box-shadow: 0 3px 6px rgba(0,0,0,0.6);
  }
  .portfolio-photo {
    width: 100%;
    height: 100%;
    border: 3px solid var(--frame-inner);
  }
  .photo--garden { background: linear-gradient(135deg, #3e5a2c 0%, #8a6a4c 55%, #d9c3a8 100%); }
  .photo--golden { background: linear-gradient(135deg, #4d6a38 0%, #c9a864 50%, #efd9a0 100%); }
  .photo--studio { background: linear-gradient(135deg, #f2f2f0 0%, #d8c2b0 60%, #8a6e5a 100%); }
  .photo--soft { background: linear-gradient(135deg, #eee8e2 0%, #c79a7c 60%, #8c5c44 100%); }
  .photo--mono { background: linear-gradient(135deg, #5e5e5e 0%, #d4d4d4 50%, #1e1e1e 100%); }
  .photo--forest { background: linear-gradient(135deg, #2f4a24 0%, #6c8a48 50%, #e6e2da 100%); }

  .contact-list {
    position: absolute;
    left: 0;
    right: 0;
    top: 175px;
    text-align: center;
    font-family: "Didact Gothic", sans-serif;
    color: var(--text-muted);
  }
  .contact-label {
    font-size: 15px;
    letter-spacing: 1px;
    text-transform: uppercase;
  }
  .contact-value {
    font-size: 17px;
    letter-spacing: 1px;
    margin: 6px 0 18px;
    color: var(--text-soft);
  }
</style>
</head>
<body>
<main class="canvas">

  <section class="card card--front" aria-label="Card front">
    <h1 class="brand-name">Mara Veldt</h1>
    <p class="brand-role">Makeup Artist</p>
    <div class="portfolio-strip">
      <div class="portfolio-frame"><div class="portfolio-photo photo--garden" role="img" aria-label="Portfolio photo: brunette model in a garden"></div></div>
      <div class="portfolio-frame"><div class="portfolio-photo photo--golden" role="img" aria-label="Portfolio photo: blonde model among flowers"></div></div>
      <div class="portfolio-frame"><div class="portfolio-photo photo--studio" role="img" aria-label="Portfolio photo: studio beauty portrait on white"></div></div>
      <div class="portfolio-frame"><div class="portfolio-photo photo--soft" role="img" aria-label="Portfolio photo: bridal hair and makeup close-up"></div></div>
      <div class="portfolio-frame"><div class="portfolio-photo photo--mono" role="img" aria-label="Portfolio photo: black and white fashion portrait"></div></div>
    </div>
  </section>

  <section class="card card--back" aria-label="Card back">
    <div class="portfolio-strip">
      <div class="portfolio-frame"><div class="portfolio-photo photo--garden" role="img" aria-label="Portfolio photo: brunette model in white dress"></div></div>
      <div class="portfolio-frame"><div class="portfolio-photo photo--golden" role="img" aria-label="Portfolio photo: blonde model with flowers"></div></div>
      <div class="portfolio-frame"><div class="portfolio-photo photo--golden" role="img" aria-label="Portfolio photo: blonde model close-up"></div></div>
      <div class="portfolio-frame"><div class="portfolio-photo photo--forest" role="img" aria-label="Portfolio photo: bride in a garden"></div></div>
      <div class="portfolio-frame"><div class="portfolio-photo photo--forest" role="img" aria-label="Portfolio photo: bride holding a bouquet"></div></div>
    </div>
    <div class="contact-list">
      <p class="contact-label">Phone Number</p>
      <p class="contact-value">0418 372 915</p>
      <p class="contact-label">Website</p>
      <p class="contact-value">www.maraveldt.com.au</p>
      <p class="contact-label">Email</p>
      <p class="contact-value">contact@maraveldt.com.au</p>
    </div>
  </section>

</main>
</body>
</html>
```